Mission Sign for Pluma-Doro Brennan & 418

I want a sign made for my company mission, purpose, and values to be on. This is a sign that will be posted for my team to see in the back of the house of a restaurant. I'd like for the design to be able to be all together with mission, purpose, and values, but also to be able to be printed with only the mission and/or purpose. These can be two designs if needed. The restaurant logo "pluma-doro" cannot be altered, but anything else can. The VIS standard for typical typical is aprecu(?), but it is not required to be used for this document since it not for the public. Red is PMS 186c. Also enclosed are our icons we use at Pluma-Doro that can be incorporated when using the values if needed.

Here is the Mission/Purpose/Values

Mission:
Be "REMARK"able

Purpose
to create a place of restoration (the "to" can be taken out if needed)

Values
Clarity
Over-Communication
Commitment
Aligned as One Team
Follow Through

Feel free to use the cursive be remarkable or another design
Feel free to make the restoration letters "restorative." It could be an old car, antique furniture, a plant coming up from the ground. Maybe the t could be a tree.

Target Market(s)

Pluma-Doro Team Members

Industry/Entity Type

Restaurant

Font styles to use
Other font styles liked:
• Aprecu

Colors
ec1f27

Requirements
Must have
• Pluma-Doro script logo
Should not have
• additional words that given in the description

```html
<!DOCTYPE html>
<html lang="en">
<head>
<meta charset="utf-8">
<title>Pluma-Doro Brennan &amp; 418 — Mission, Purpose, Values</title>
<link rel="stylesheet" href="https://fonts.googleapis.com/css2?family=Open+Sans:wght@700&family=Leckerli+One&display=swap">
<style>
  :root {
    --brand-red: #c8102e;
    --paper: #ffffff;
    --backdrop: #ececec;
    --script: "Leckerli One", cursive;
    --sans: "Open Sans", sans-serif;
  }
  * { box-sizing: border-box; margin: 0; padding: 0; }
  html, body { width: 1200px; height: 1000px; overflow: hidden; background: var(--backdrop); }

  .sign {
    position: absolute; left: 283px; top: 10px;
    width: 650px; height: 975px;
    background: var(--paper);
    color: var(--brand-red);
  }

  .brand {
    position: absolute; top: 44px; left: 0; width: 100%;
    text-align: center;
    font-family: var(--sans); font-weight: 700; color: var(--brand-red);
  }
  .brand__name { font-size: 34px; line-height: 40px; }
  .brand__location { margin-top: 10px; font-size: 19px; line-height: 24px; }

  .panel {
    position: absolute; left: 33px; width: 581px;
    border: 4px dotted var(--brand-red);
    display: flex; flex-direction: column; align-items: center; justify-content: center;
    text-align: center;
  }
  .panel__label {
    position: absolute; top: -14px; left: 50%; transform: translateX(-50%);
    padding: 0 12px;
    background: var(--paper);
    font-family: var(--sans); font-weight: 700; font-size: 19px; line-height: 24px;
    letter-spacing: 0.5px;
  }

  .mission { top: 170px; height: 197px; }
  .mission__text { font-family: var(--script); font-size: 67px; line-height: 1; margin-top: 12px; }

  .purpose-band {
    position: absolute; left: 0; top: 393px; width: 100%; height: 267px;
    background: var(--brand-red);
  }
  .purpose { top: 24px; height: 218px; border-color: var(--paper); color: var(--paper); }
  .purpose .panel__label { background: var(--brand-red); top: -14px; }
  .purpose__lead { font-family: var(--script); font-size: 54px; line-height: 1; margin-top: 14px; }
  .purpose__key { font-family: var(--script); font-size: 87px; line-height: 1; margin-top: 2px; }

  .values { top: 687px; height: 255px; padding-top: 16px; }
  .values__list { list-style: none; }
  .values__item {
    display: flex; align-items: center; justify-content: center; gap: 10px;
    font-family: var(--script); font-size: 34px; line-height: 38px;
  }
  .tick { width: 15px; height: 15px; flex: none; }
  .tick--hidden { visibility: hidden; }
</style>
</head>
<body>
  <svg width="0" height="0" style="position:absolute" aria-hidden="true">
    <symbol id="tick" viewBox="0 0 16 16">
      <circle cx="8" cy="8" r="8" fill="#c8102e"/>
      <path d="M4.3 8.3 L7 10.8 L11.8 5.4" fill="none" stroke="#fff" stroke-width="1.9" stroke-linecap="round" stroke-linejoin="round"/>
    </symbol>
  </svg>

  <main class="sign">
    <header class="brand">
      <div class="brand__name">Pluma-Doro</div>
      <div class="brand__location">Brennan &amp; 418</div>
    </header>

    <section class="panel mission">
      <h2 class="panel__label">MISSION</h2>
      <p class="mission__text">be remarkable</p>
    </section>

    <div class="purpose-band">
      <section class="panel purpose">
        <h2 class="panel__label">PURPOSE</h2>
        <p class="purpose__lead">create a place of</p>
        <p class="purpose__key">restoration</p>
      </section>
    </div>

    <section class="panel values">
      <h2 class="panel__label">VALUES</h2>
      <ul class="values__list">
        <li class="values__item"><svg class="tick"><use href="#tick"/></svg>clarity<svg class="tick"><use href="#tick"/></svg></li>
        <li class="values__item"><svg class="tick"><use href="#tick"/></svg>over-communication<svg class="tick"><use href="#tick"/></svg></li>
        <li class="values__item"><svg class="tick tick--hidden"><use href="#tick"/></svg>commitment<svg class="tick"><use href="#tick"/></svg></li>
        <li class="values__item"><svg class="tick"><use href="#tick"/></svg>aligned as one team<svg class="tick"><use href="#tick"/></svg></li>
        <li class="values__item"><svg class="tick"><use href="#tick"/></svg>follow through<svg class="tick"><use href="#tick"/></svg></li>
      </ul>
    </section>
  </main>
</body>
</html>
```